Business Cards, Letterhead and Email signature for Halvern Building Collective
Halvern Building Collective
Professional
Doran Pellick
Partner
Office: 4100 Birchmont Ave Suite 900 Charlotte, NC 28211
Mailing: 5217 Birchmont Ave #482 Charlotte, NC 28211
dpellick@halvernbuildingcoll.example
halvvernbuildingcoll.example
I am open to ideas, maybe the logo with a matching background color. Be creative

```html
<!DOCTYPE html>
<html lang="en">
<head>
<meta charset="utf-8">
<title>Halvern Building Collective – Business Cards</title>
<link href="https://fonts.googleapis.com/css2?family=Open+Sans:wght@400;600;700;800&display=swap" rel="stylesheet">
<style>
  :root {
    --stage: #d9dadc;
    --card-white: #ffffff;
    --brand-blue: #1d4f9c;
    --brand-blue-deep: #0e2f66;
    --ink: #4a4d52;
    --ink-soft: #6d7076;
    --ink-strong: #34373c;
    --steel-light: #eceef0;
    --steel-mid: #c4c7cb;
    --steel-dark: #8d9196;
  }
  * { margin: 0; padding: 0; box-sizing: border-box; }
  html, body {
    width: 1200px; height: 901px; overflow: hidden;
    background: var(--stage);
    font-family: "Open Sans", Arial, sans-serif;
  }
  .canvas { position: relative; width: 1200px; height: 901px; }

  .card {
    position: absolute; width: 620px; height: 354px; overflow: hidden;
    border-radius: 4px;
    box-shadow: 0 6px 18px rgba(0,0,0,0.18);
  }

  /* Back card */
  .card-back {
    left: 60px; top: 70px;
    background: linear-gradient(135deg, var(--brand-blue) 0%, var(--brand-blue-deep) 100%);
  }
  .card-back .building-art {
    position: absolute; left: 0; top: 0; width: 620px; height: 354px;
  }
  .card-back .brand-name {
    position: absolute; left: 30px; top: 78px;
    color: #ffffff; font-weight: 800; line-height: 1;
  }
  .brand-name .word-main { display: block; font-size: 34px; letter-spacing: 1px; }
  .brand-name .word-sub { display: block; font-size: 12.5px; letter-spacing: 1.4px; margin-top: 3px; }
  .card-back .web {
    position: absolute; right: 30px; bottom: 24px;
    font-size: 13px; color: var(--ink-strong); letter-spacing: 0.3px;
    white-space: nowrap;
  }

  /* Front card */
  .card-front { left: 520px; top: 470px; background: var(--card-white); }
  .card-front .building-art {
    position: absolute; left: 0; top: 0; width: 620px; height: 354px;
  }
  .card-front .logo-lockup {
    position: absolute; right: 34px; top: 52px;
    display: flex; align-items: center; gap: 12px;
    color: var(--brand-blue);
  }
  .logo-lockup .logo-square {
    width: 46px; height: 46px; background: var(--brand-blue);
  }
  .logo-lockup .brand-name { font-weight: 800; line-height: 1; }
  .logo-lockup .word-main { font-size: 40px; }
  .logo-lockup .word-sub { font-size: 14.5px; letter-spacing: 1.3px; }

  .contact { position: absolute; left: 34px; top: 46px; color: var(--ink); }
  .contact .person-name { font-size: 17px; font-weight: 600; color: var(--brand-blue); }
  .contact .person-title { font-size: 11.5px; color: var(--ink-soft); margin-top: 1px; }
  .contact .address { font-size: 12px; line-height: 1.3; margin-top: 14px; }
  .contact .channels { list-style: none; margin-top: 14px; font-size: 12px; line-height: 1.38; }
  .channels li { display: flex; align-items: center; gap: 6px; white-space: nowrap; }
  .channels svg { width: 11px; height: 11px; fill: var(--brand-blue); flex: none; }
</style>
</head>
<body>
<main class="canvas">

  <section class="card card-back">
    <svg class="building-art" viewBox="0 0 620 354" role="img" aria-label="Stepped building facade graphic in white and grey">
      <defs>
        <linearGradient id="steelBack" x1="0" y1="0" x2="1" y2="1">
          <stop offset="0" stop-color="#eceef0"/>
          <stop offset="0.6" stop-color="#c4c7cb"/>
          <stop offset="1" stop-color="#8d9196"/>
        </linearGradient>
      </defs>
      <polygon points="150,354 620,70 620,354" fill="url(#steelBack)"/>
    </svg>
    <div class="brand-name">
      <span class="word-main">HALVERN</span>
      <span class="word-sub">BUILDING COLLECTIVE</span>
    </div>
    <div class="web">www.halvernbuildingcoll.example</div>
  </section>

  <section class="card card-front">
    <svg class="building-art" viewBox="0 0 620 354" role="img" aria-label="Stepped building facade graphic in light grey">
      <defs>
        <linearGradient id="steelFront" x1="0" y1="0" x2="1" y2="1">
          <stop offset="0" stop-color="#f4f5f6"/>
          <stop offset="0.6" stop-color="#c9ccd0"/>
          <stop offset="1" stop-color="#6f7378"/>
        </linearGradient>
      </defs>
      <polygon points="330,354 620,200 620,354" fill="url(#steelFront)"/>
    </svg>

    <div class="contact">
      <p class="person-name">Doran Pellick</p>
      <p class="person-title">Partner</p>
      <p class="address">Office: 4100 Birchmont Ave Suite 900<br>Charlotte, NC 28211</p>
      <p class="address">Mailing: 5217 Birchmont Ave #482<br>Charlotte, NC 28211</p>
      <ul class="channels">
        <li><svg viewBox="0 0 12 12"><path d="M2.5 1h2l1 2.5-1.3 1a6 6 0 0 0 3.3 3.3l1-1.3L11 7.5v2a1 1 0 0 1-1 1A9 9 0 0 1 1.5 2a1 1 0 0 1 1-1z"/></svg>555 310 2741</li>
        <li><svg viewBox="0 0 12 12"><rect x="3" y="0.5" width="6" height="11" rx="1"/><rect x="4" y="2" width="4" height="6.5" fill="#fff"/></svg>555 310 8862</li>
        <li><svg viewBox="0 0 12 12"><rect x="1" y="4" width="10" height="6" rx="1"/><rect x="3" y="1" width="6" height="3"/></svg>555 310 2749</li>
        <li><svg viewBox="0 0 12 12"><rect x="0.5" y="2" width="11" height="8" rx="1"/><path d="M1 2.5 6 6.5l5-4" stroke="#fff" fill="none"/></svg>dpellick@halvernbuildingcoll.example</li>
        <li><svg viewBox="0 0 12 12"><circle cx="6" cy="6" r="5.5"/><path d="M0.5 6h11M6 0.5c-3 3-3 8 0 11m0-11c3 3 3 8 0 11" stroke="#fff" stroke-width="0.8" fill="none"/></svg>www.halvernbuildingcoll.example</li>
      </ul>
    </div>

    <div class="logo-lockup">
      <span class="logo-square"></span>
      <div class="brand-name">
        <span class="word-main">HALVERN</span>
        <span class="word-sub">BUILDING COLLECTIVE</span>
      </div>
    </div>
  </section>

</main>
</body>
</html>
```